Just upload my Logo
Simple
Elsa Marroquín
quillmarshimages@postnook.net
Follow me in Chatterloom
* Wedding
* Engagment
* Maternity
* Newborn
* Family
* Events......etc

```html
<!DOCTYPE html>
<html lang="en">
<head>
<meta charset="utf-8">
<title>Quillmarsh Images – Business Card</title>
<link href="https://fonts.googleapis.com/css2?family=Tinos:ital,wght@0,400;0,700;1,400&display=swap" rel="stylesheet">
<style>
  :root {
    --backdrop: #d9d9d9;
    --card: #ffffff;
    --charcoal: #3a3a3c;
    --pink: #e8469b;
    --ink: #2b2b2b;
    --rule: #9a9a9a;
    --art-light: #e4e4e4;
    --art-dark: #8c8c8c;
  }
  * { margin: 0; padding: 0; box-sizing: border-box; }
  html, body {
    width: 1200px;
    height: 1050px;
    overflow: hidden;
    background: var(--backdrop);
    font-family: "Tinos", "Times New Roman", serif;
  }
  .business-card {
    position: absolute;
    left: 75px;
    top: 225px;
    width: 1050px;
    height: 600px;
    border-radius: 34px;
    overflow: hidden;
    background: var(--card);
    box-shadow: 0 6px 18px rgba(0,0,0,0.18);
  }
  .card-corners {
    position: absolute;
    inset: 0;
    width: 100%;
    height: 100%;
  }
  .logo-art {
    position: absolute;
    left: 200px;
    top: 85px;
    width: 200px;
    height: 170px;
    border-radius: 10px;
    background: linear-gradient(135deg, var(--art-light), var(--art-dark));
  }
  .brand {
    position: absolute;
    left: 418px;
    top: 138px;
    color: var(--pink);
  }
  .brand-name {
    font-size: 50px;
    font-weight: 400;
    line-height: 1;
    letter-spacing: 1px;
  }
  .brand-byline {
    margin-top: 10px;
    padding-left: 150px;
    font-size: 24px;
    color: var(--ink);
    font-style: italic;
  }
  .owner-name {
    position: absolute;
    left: 112px;
    top: 448px;
    font-size: 34px;
    font-weight: 700;
    color: var(--ink);
  }
  .divider {
    position: absolute;
    left: 408px;
    top: 400px;
    width: 1px;
    height: 136px;
    background: var(--rule);
  }
  .contact-list {
    position: absolute;
    left: 428px;
    top: 400px;
    list-style: none;
    font-size: 23px;
    color: var(--ink);
  }
  .contact-item {
    display: flex;
    align-items: center;
    gap: 12px;
    height: 40px;
  }
  .contact-icon { width: 22px; height: 22px; flex: none; }
  .services {
    position: absolute;
    left: 428px;
    top: 540px;
    font-size: 18px;
    letter-spacing: 0.5px;
    color: var(--pink);
  }
</style>
</head>
<body>
  <section class="business-card">
    <svg class="card-corners" viewBox="0 0 1050 600" aria-hidden="true">
      <path d="M690 0 Q960 30 1050 290 L1050 0 Z" fill="var(--charcoal)"/>
      <path d="M690 0 Q960 30 1050 290" fill="none" stroke="var(--pink)" stroke-width="8"/>
      <path d="M0 300 Q60 540 360 600 L0 600 Z" fill="var(--charcoal)"/>
      <path d="M0 300 Q60 540 360 600" fill="none" stroke="var(--pink)" stroke-width="8"/>
    </svg>

    <div class="logo-art" role="img" aria-label="Ornamental bird illustration perched on a flourish branch"></div>

    <div class="brand">
      <div class="brand-name">Quillmarsh Images</div>
      <div class="brand-byline">by Elsa Marroquín</div>
    </div>

    <h1 class="owner-name">Elsa Marroquín</h1>
    <div class="divider"></div>

    <ul class="contact-list">
      <li class="contact-item">
        <svg class="contact-icon" viewBox="0 0 24 24" aria-hidden="true">
          <rect x="6" y="2" width="12" height="20" rx="2.5" fill="none" stroke="var(--pink)" stroke-width="2"/>
          <circle cx="12" cy="18" r="1.3" fill="var(--pink)"/>
        </svg>
        <span>(555) 318-2740</span>
      </li>
      <li class="contact-item">
        <svg class="contact-icon" viewBox="0 0 24 24" aria-hidden="true">
          <rect x="3" y="6" width="18" height="12" rx="1.5" fill="none" stroke="var(--pink)" stroke-width="2"/>
          <path d="M3.5 7 L12 13 L20.5 7" fill="none" stroke="var(--pink)" stroke-width="2"/>
        </svg>
        <span>quillmarshimages@postnook.net</span>
      </li>
      <li class="contact-item">
        <svg class="contact-icon" viewBox="0 0 24 24" aria-hidden="true">
          <circle cx="12" cy="12" r="8" fill="none" stroke="var(--pink)" stroke-width="2"/>
        </svg>
        <span>Follow me in Chatterloom</span>
      </li>
    </ul>

    <p class="services">Wedding · Engagement · Maternity · Newborn · Family · Events</p>
  </section>
</body>
</html>
```